Stationary for Real Estate Investor
Holvane Estates
Stationary for Real Estate Investor - Real Estate
Creative Brief
Simple
Teodoro Vilchis
Real Estate Investor
P.O Box 417, Castro Ridge, CA 94812
teodoro@holvaneestates.example
Only use address on envelope (back flap, small print) Logo in Front Corner On letterhead only use logo (no contact info)
tvilchis27 tvilchis27
No Address on business card only on envelope.

```html
<!DOCTYPE html>
<html lang="en">
<head>
<meta charset="utf-8">
<title>Holvane Estates — Business Card</title>
<link rel="stylesheet" href="https://fonts.googleapis.com/css2?family=Montserrat:wght@400;600;700;800&display=swap">
<style>
  :root {
    --backdrop: #3a3a3c;
    --card: #ffffff;
    --ink: #1c1c1c;
    --ink-soft: #5a5a5a;
    --band: #161616;
    --tile-mid: #7d7d7d;
    --tile-light: #bdbdbd;
  }
  * { box-sizing: border-box; margin: 0; padding: 0; }
  html, body { width: 1200px; height: 1077px; overflow: hidden; }
  body {
    background: var(--backdrop);
    font-family: "Montserrat", sans-serif;
    color: var(--ink);
    position: relative;
  }
  .card {
    position: absolute;
    left: 170px;
    width: 860px;
    height: 491px;
    background: var(--card);
    overflow: hidden;
  }
  .card--back { top: 30px; }
  .card--front { top: 556px; }

  .company-name {
    position: absolute;
    white-space: nowrap;
    font-weight: 600;
    color: var(--ink);
    letter-spacing: 0.04em;
    text-transform: uppercase;
  }

  .block-title { font-weight: 800; font-size: 17px; letter-spacing: 0.04em; text-transform: uppercase; margin-bottom: 6px; }
  .block-line { font-weight: 400; font-size: 14px; line-height: 1.45; color: var(--ink-soft); }

  .contact { position: absolute; left: 56px; top: 48px; }
  .social { position: absolute; right: 56px; top: 48px; text-align: right; }
  .card--back .company-name { left: 56px; top: 222px; font-size: 34px; }

  .holder { position: absolute; right: 56px; top: 300px; text-align: right; }
  .holder__name { font-weight: 700; font-size: 26px; text-transform: uppercase; letter-spacing: 0.02em; }
  .holder__role { font-weight: 600; font-size: 14px; text-transform: uppercase; letter-spacing: 0.08em; margin-top: 4px; }

  .band { position: absolute; left: 0; bottom: 0; width: 100%; height: 60px; }

  .card--front .company-name { left: 90px; top: 190px; font-size: 50px; }
  .front-bar { position: absolute; left: 0; bottom: 0; width: 100%; height: 28px; background: var(--band); }
</style>
</head>
<body>
  <section class="card card--back" aria-label="Business card, back">
    <div class="contact">
      <p class="block-title">Contact Us</p>
      <p class="block-line">555 014 2290</p>
      <p class="block-line">teodoro@holvaneestates.example</p>
      <p class="block-line">www.holvaneestates.example</p>
    </div>
    <div class="social">
      <p class="block-title">Follow Us on Social</p>
      <p class="block-line">friendspace.example/tvilchis27</p>
      <p class="block-line">chirper.example/tvilchis27</p>
      <p class="block-line">folioboard.example/tvilchis27</p>
    </div>
    <p class="company-name">Holvane Estates</p>
    <div class="holder">
      <p class="holder__name">Teodoro Vilchis</p>
      <p class="holder__role">Real Estate Investor</p>
    </div>
    <svg class="band" viewBox="0 0 860 60" preserveAspectRatio="none" aria-hidden="true">
      <rect x="0" y="0" width="860" height="60" fill="var(--band)"/>
      <rect x="40" y="0" width="40" height="60" fill="var(--tile-mid)"/>
      <rect x="100" y="0" width="40" height="60" fill="var(--tile-light)"/>
      <rect x="160" y="0" width="40" height="60" fill="var(--tile-mid)"/>
    </svg>
  </section>

  <section class="card card--front" aria-label="Business card, front">
    <p class="company-name">Holvane Estates</p>
    <div class="front-bar"></div>
  </section>
</body>
</html>
```